Food product label for new company

2 x 4 label, red or burgundy color background, would like to take same label design and be able to change colors for product variations,
Velmora Roasted Pecan Spread
All natural, no sugar added, non-GMO, Gluten Free, No Preservatives, Low glycemic index
10oz, produced by Velmora Foods, Alder Falls, OH
Ingredients: Toasted Pecans
Instructions: Stir and Enjoy!
Cannot use Organic until certified to be or

```html
<!DOCTYPE html>
<html lang="en">
<head>
<meta charset="utf-8">
<title>Velmora Roasted Pecan Spread – Label</title>
<link rel="stylesheet" href="https://fonts.googleapis.com/css2?family=Noticia+Text:wght@400;700&family=Libre+Caslon+Text:wght@400&family=Ephesis&display=swap">
<style>
  :root {
    --page: #ffffff;
    --burgundy: #7f0b12;
    --burgundy-mid: #98262d;
    --burgundy-edge: #b5545a;
    --ink-light: #fbf6f2;
    --gold-light: #f3ead2;
    --gold: #c9a66b;
    --gold-dark: #a8824a;
  }
  * { margin: 0; padding: 0; box-sizing: border-box; }
  html, body { width: 1200px; height: 1200px; overflow: hidden; background: var(--page); }
  .canvas { position: relative; width: 1200px; height: 1200px; }

  .label {
    position: absolute; left: 100px; top: 270px; width: 1000px; height: 660px;
    background: linear-gradient(90deg, var(--burgundy-edge) 0%, var(--burgundy-mid) 22%, var(--burgundy) 48%, var(--burgundy-mid) 76%, var(--burgundy-edge) 100%);
    color: var(--ink-light);
    font-family: "Noticia Text", Georgia, serif;
  }

  .side-claim {
    position: absolute; top: 70px; height: 470px;
    writing-mode: vertical-rl; transform: rotate(180deg);
    font-family: "Libre Caslon Text", Georgia, serif;
    font-size: 17px; letter-spacing: 3.5px; line-height: 30px;
    text-transform: uppercase; text-align: center;
  }
  .side-claim--left { left: 108px; }
  .side-claim--right { right: 108px; }

  .brand {
    position: absolute; left: 0; right: 0; top: 62px;
    display: flex; justify-content: center; align-items: center; gap: 14px;
    font-weight: 700; font-size: 56px; line-height: 1;
  }
  .brand-mark { width: 16px; height: 16px; background: var(--ink-light); }

  .variant {
    position: absolute; left: 480px; top: 128px;
    font-family: "Ephesis", cursive; font-size: 72px; line-height: 1;
  }

  .product-name {
    position: absolute; left: 0; right: 0; top: 212px;
    text-align: center; font-weight: 700; line-height: 0.95; font-size: 128px;
    letter-spacing: -1px;
  }

  .tagline {
    position: absolute; left: 0; right: 0; top: 470px;
    text-align: center; font-family: "Libre Caslon Text", Georgia, serif;
    font-size: 22px; letter-spacing: 4px;
  }

  .badges {
    position: absolute; left: 0; right: 0; top: 512px;
    display: flex; justify-content: center; align-items: center; gap: 30px;
    font-size: 20px; line-height: 24px;
  }
  .badge-text--left { text-align: right; }
  .badge-text--right { text-align: left; }
  .badge-icon { width: 66px; height: 58px; border-radius: 6px;
    background: radial-gradient(circle, var(--gold) 0%, var(--gold-dark) 80%); opacity: 0.85; }

  .net-weight-row {
    position: absolute; left: 0; right: 0; top: 598px;
    display: flex; align-items: center; gap: 16px;
    font-weight: 700; font-size: 22px;
  }
  .gold-rule { flex: 1; height: 7px;
    background: linear-gradient(90deg, var(--gold-dark), var(--gold-light) 50%, var(--gold)); }
  .net-weight { white-space: nowrap; }
</style>
</head>
<body>
<div class="canvas">
  <section class="label">
    <p class="side-claim side-claim--left">No sugar added. No preservatives.<br>Low glycemic index</p>
    <p class="side-claim side-claim--right">Produced by<br>Velmora Foods. Alder Falls, OH</p>

    <div class="brand"><span class="brand-mark"></span><span class="brand-name">Velmora</span></div>
    <div class="variant">Roasted</div>
    <h1 class="product-name">PECAN<br>SPREAD</h1>
    <p class="tagline">- ALL NATURAL -</p>

    <div class="badges">
      <span class="badge-text--left">GLUTEN<br>FREE</span>
      <div class="badge-icon" role="img" aria-label="Gold sprout and field emblem"></div>
      <span class="badge-text--right">GMO<br>FREE</span>
    </div>

    <div class="net-weight-row">
      <span class="gold-rule"></span>
      <span class="net-weight">Net.Wt. 10oz (283g)</span>
      <span class="gold-rule"></span>
    </div>
  </section>
</div>
</body>
</html>
```